Web Design for Rubbish Removal Company

I am looking for a custom web design that is clean and modern which also has a professional trustworthy feel to it.
The website is http://www.kendrawaste.com.au/ and need:
1 x Front Page
1 x Location Page
Please keep the green colour scheme as this is the corporate colours but would like to steer away from the black.
Industry/Entity Type
It Company
Number of Pages Required
2 page
Font styles to use
Sans Serif
Requirements
Must have
- Clean & Professional
- Keep green colour scheme
Should not have
- Steer away from black
- not look like a template

```html
<!DOCTYPE html>
<html lang="en">
<head>
<meta charset="utf-8">
<title>Kendra Waste Removal</title>
<link href="https://fonts.googleapis.com/css2?family=Open+Sans:wght@400;600;700&family=Raleway:wght@400;600;700&display=swap" rel="stylesheet">
<style>
:root{
  --green:#7cbf2a;
  --green-dark:#5e9c17;
  --green-light:#a6d65e;
  --ink:#4a4a4a;
  --muted:#8a8a8a;
  --line:#e2e2e2;
  --paper:#ffffff;
  --wood:#eceae6;
  --wood-dark:#d9d6d0;
}
*{box-sizing:border-box;margin:0;padding:0}
html,body{width:788px;height:1200px;overflow:hidden}
body{font-family:"Open Sans",Arial,sans-serif;color:var(--ink);background:linear-gradient(180deg,var(--wood) 0%,#f3f2ef 100%);position:relative}
.site-header{position:absolute;top:0;left:0;width:788px;height:38px;background:var(--paper);display:flex;align-items:center;justify-content:space-between;padding:0 28px 0 30px;border-bottom:1px solid var(--line)}
.brand{font-family:"Raleway",Arial,sans-serif;font-weight:700;font-size:15px;color:var(--green-dark);letter-spacing:.3px;text-transform:uppercase}
.main-nav{display:flex;gap:22px;font-family:"Raleway",Arial,sans-serif;font-size:9px;font-weight:700;color:var(--ink);letter-spacing:.5px}
.hero{position:absolute;top:38px;left:0;width:788px;height:380px;background:repeating-linear-gradient(90deg,var(--wood) 0 58px,var(--wood-dark) 58px 60px)}
.hero-photo{position:absolute;left:40px;top:0;width:300px;height:380px;background:linear-gradient(180deg,#d7c8b8 0%,#b9a392 55%,#9a9a9c 100%);border-radius:120px 120px 0 0}
.badge{position:absolute;left:448px;top:28px;width:74px;height:74px;border-radius:50%;background:radial-gradient(circle,#d23a2e 0 45%,#e0b040 46% 100%)}
.hero-title{position:absolute;left:395px;top:120px;width:360px;text-align:center;font-family:"Raleway",Arial,sans-serif;font-weight:700;font-size:26px;line-height:31px;color:var(--green);text-transform:uppercase}
.hero-points{position:absolute;left:430px;top:218px;list-style:none;font-size:15px;line-height:24px;color:var(--ink)}
.hero-points li::before{content:"•";margin-right:10px}
.ribbon{position:absolute;top:392px;left:0;width:788px;height:34px;background:linear-gradient(180deg,var(--green-light),var(--green));clip-path:polygon(0 0,100% 30%,100% 100%,0 100%)}
.content-card{position:absolute;top:426px;left:30px;width:728px;height:730px;background:var(--paper);box-shadow:0 0 6px rgba(0,0,0,.12)}
.services{display:flex;padding:20px 18px 0;gap:16px}
.service{flex:1;display:flex;align-items:center;gap:12px;border-bottom:2px solid var(--line);padding-bottom:14px}
.service svg{flex:none}
.service h3{font-family:"Raleway",Arial,sans-serif;font-size:13px;font-weight:600;color:var(--green);text-transform:uppercase;line-height:17px}
.offer-list{position:absolute;left:22px;top:110px;width:380px;list-style:none;font-size:9.5px;line-height:14px;color:var(--ink)}
.offer-list li{margin-bottom:14px}
.gallery{position:absolute;left:426px;top:96px;width:284px;height:260px}
.gallery-photo{position:absolute;top:0;width:140px;height:230px;background:linear-gradient(180deg,#7a9a58 0%,#9aa06a 50%,#8d7758 100%)}
.gallery-photo.after{left:144px;background:linear-gradient(180deg,#8aa862 0%,#b0b07a 55%,#a08868 100%)}
.gallery-tag{position:absolute;bottom:12px;width:100px;left:20px;border:1px solid #fff;color:#fff;font-size:10px;letter-spacing:1px;text-align:center;padding:3px 0;background:rgba(0,0,0,.25)}
.gallery-nav{position:absolute;top:240px;left:0;width:284px;display:flex;justify-content:space-between;align-items:center;font-size:8px;color:var(--muted)}
.dot{width:12px;height:12px;border-radius:50%;background:var(--green)}
.section-head{position:absolute;top:430px;display:flex;align-items:baseline;gap:10px;border-bottom:2px solid var(--line);padding-bottom:8px;width:340px}
.section-head h2{font-family:"Raleway",Arial,sans-serif;font-size:16px;font-weight:400;color:var(--green);text-transform:uppercase}
.section-head span{font-size:10px;font-weight:600;color:var(--ink)}
.book-head{left:22px}
.testi-head{left:366px}
.payments-label{position:absolute;left:22px;top:600px;width:340px;text-align:center;font-size:12px;color:var(--ink)}
.payments{position:absolute;left:22px;top:636px;width:340px;display:flex;justify-content:center;gap:18px}
.pay-card{width:58px;height:32px;border:1px solid var(--line);display:flex;align-items:center;justify-content:center;font-size:8px;font-weight:700;color:var(--ink)}
.book-btn{position:absolute;left:142px;top:694px;width:100px;height:28px;background:var(--green);border-radius:3px;color:#fff;font-size:10px;font-weight:700;text-align:center;line-height:28px}
.testimonials{position:absolute;left:366px;top:476px;width:340px;list-style:none}
.testimonial{display:flex;gap:14px;margin-bottom:14px;border-bottom:1px solid var(--line);padding-bottom:10px}
.testimonial .mark{flex:none;width:20px;height:20px;border-radius:50%;border:2px solid var(--green);margin-top:18px;position:relative}
.testimonial .mark::after{content:"";position:absolute;inset:5px;border-radius:50%;background:var(--green)}
.testimonial p{font-size:8.5px;line-height:12px;color:var(--ink)}
.testimonial cite{display:block;text-align:right;font-size:7px;font-style:italic;color:var(--green-dark);margin-top:4px}
.testi-nav{position:absolute;left:676px;top:708px;display:flex;gap:6px;align-items:center;font-size:7px;color:var(--muted)}
.site-footer{position:absolute;top:1172px;left:0;width:788px;text-align:center;font-size:8px;color:var(--muted)}
</style>
</head>
<body>
<header class="site-header">
  <div class="brand">Kendra Waste Removal</div>
  <nav class="main-nav"><span>HOME</span><span>ABOUT</span><span>SERVICES</span><span>GALLERY</span><span>FAQS</span><span>BLOG</span><span>CONTACT</span></nav>
</header>

<section class="hero">
  <div class="hero-photo" role="img" aria-label="Smiling removal worker giving a thumbs up"></div>
  <div class="badge" role="img" aria-label="Satisfaction guarantee seal"></div>
  <h1 class="hero-title">Sydney's Cheapest Rubbish Removal Services</h1>
  <ul class="hero-points">
    <li>Free Quote</li>
    <li>Cheapest prize</li>
    <li>Always on Time</li>
    <li>More than 10 years of experience</li>
  </ul>
</section>
<div class="ribbon"></div>

<main class="content-card">
  <div class="services">
    <div class="service">
      <svg width="36" height="34" viewBox="0 0 36 34" fill="none" stroke="#7cbf2a" stroke-width="2"><path d="M3 16 18 3l15 13"/><path d="M7 13v18h22V13"/><rect x="15" y="20" width="6" height="11"/></svg>
      <h3>Household Rubbish<br>Removals</h3>
    </div>
    <div class="service">
      <svg width="36" height="34" viewBox="0 0 36 34" fill="none" stroke="#7cbf2a" stroke-width="2"><rect x="4" y="10" width="28" height="20"/><path d="M13 10V5h10v5M4 18h28"/></svg>
      <h3>Office Rubbish<br>Removals</h3>
    </div>
    <div class="service">
      <svg width="36" height="34" viewBox="0 0 36 34" fill="none" stroke="#7cbf2a" stroke-width="2"><path d="M4 31h28M8 31V6h20v25M8 14h20M8 22h20M15 6v25M22 6v25"/></svg>
      <h3>Construction Rubbish<br>Removals</h3>
    </div>
  </div>

  <ul class="offer-list">
    <li>Complete rubbish clean-out including demolition, strip outs and labour hire</li>
    <li>Removal of white goods, garden rubbish, furniture and more</li>
    <li>No job is too large, too small or too difficult</li>
    <li>Extra discounts for returning customers</li>
    <li>Free quote provided with all enquiries</li>
    <li>Over 10 years in the rubbish removal trade</li>
    <li>Same day rubbish and waste collection</li>
    <li>CHEAPEST PRICES in Sydney</li>
  </ul>

  <div class="gallery">
    <div class="gallery-photo" role="img" aria-label="Garden yard full of rubbish before removal"><span class="gallery-tag">BEFORE</span></div>
    <div class="gallery-photo after" role="img" aria-label="Same garden yard cleared after removal"><span class="gallery-tag">AFTER</span></div>
    <div class="gallery-nav"><span class="dot"></span><span>1 of 3</span><span class="dot"></span></div>
  </div>

  <div class="section-head book-head"><h2>Book</h2><span>Schedule an appointment</span></div>
  <div class="section-head testi-head"><h2>Testimonials</h2><span>What our customers said</span></div>

  <p class="payments-label">We accept payments from</p>
  <div class="payments">
    <div class="pay-card">Vantix</div>
    <div class="pay-card">Orbit Pay</div>
    <div class="pay-card">Tapline</div>
  </div>
  <div class="book-btn">BOOK HERE</div>

  <ul class="testimonials">
    <li class="testimonial">
      <span class="mark"></span>
      <div>
        <p>Excellent service, quick quote on the spot for a major clean up of household rubbish. The team provided a quick, efficient and courteous removal. Very satisfied customer.</p>
        <cite>Lara Hemsworth - Bondi, Sydney</cite>
      </div>
    </li>
    <li class="testimonial">
      <span class="mark"></span>
      <div>
        <p>We needed a few days to come down to the building site and remove large amounts of material after demolition. Staff were very friendly and gave us all the info we needed. The crew arrived on time and got the job done. Top job mate!</p>
        <cite>Marcus Dell - Parramatta, Sydney</cite>
      </div>
    </li>
  </ul>
  <div class="testi-nav"><span>1 of 6</span><span class="dot"></span></div>
</main>

<footer class="site-footer">Copyright © Kendra Waste Removal. All rights reserved.</footer>
</body>
</html>
```